THE KINDLING LANTERN

project description

The Kindling Lantern was created to challenge the lack of meaning and values in power of mainstream media.

This website will be a platform through which you can explore the meaning of humanity, through a variety of lenses - philosophy, politics, science, art, human interest stories, etc.

As an organization, TKL aims to further the understanding of the meaning of humanity, including its spiritual and existential challenges in 21st century. We wish to inspire and develop this understanding, while transforming mass media and “visual” spaces so they display the beauty and interconnectedness of human beings.

We believe that The Kindling Lantern and that our “visual” space and mass media should reflect and support those values.

We are looking to create an image that may be seen on the site independently, full screen - or as the background to the home page (with text on top of it, potentially.)
Updates

 

 The city/the background with the advertisementshouldn’t be to depressing because (indigo blue or light gray color) so overall, the page has a pleasant soft look and feel.

 

Also place the boy is looking at needs to have advertisement

 

Thank you

Target Market(s)

people that are sophisticated, modern, engage, care, awere, who are interested scholarly discussions of media, philosophy,art/desighn community - as well as the human spirit.

Industry/Entity Type

Media

Requirements
Must have
• I have photos of a boy looking up. I would like to take this image (pick one) and incorporate into a city scene - one with buildings littered with mass media information and adds - similar to the look of NYC's Wexford Plaza. He is looking up a bit overwhelmed trying to make sense of the world he is seeing.
Nice to have
• However, the city scene in the background may be sketched or distorted
Should not have
• should not be agresive or too busy

```html
<!DOCTYPE html>
<html lang="en">
<head>
<meta charset="utf-8">
<title>The Kindling Lantern</title>
<link href="https://fonts.googleapis.com/css2?family=Istok+Web:wght@400;700&family=Ubuntu:wght@400;500;700&display=swap" rel="stylesheet">
<style>
:root{
  --navy:#17405f;
  --navy-deep:#0f3150;
  --navy-line:#2f5473;
  --ink:#14365a;
  --orange:#fba11a;
  --orange-dark:#f29a12;
  --light:#e4e4e4;
  --white:#ffffff;
  --muted:#c9d3dc;
}
*{margin:0;padding:0;box-sizing:border-box}
html,body{width:910px;height:1200px;overflow:hidden;background:var(--navy)}
body{font-family:"Istok Web",Verdana,sans-serif;color:var(--white)}
.page{position:relative;width:910px;height:1200px;overflow:hidden;background:var(--navy)}
.abs{position:absolute}
a{color:inherit;text-decoration:none}

.top-stripe{left:0;top:24px;width:910px;height:5px;background:var(--light)}
.util-nav{left:569px;top:0;width:277px;height:26px;background:var(--light);color:var(--ink);font-size:9px;letter-spacing:.3px;display:flex;align-items:center;justify-content:center;gap:10px}

.brand{left:65px;top:40px;display:flex;align-items:center;gap:12px}
.brand-mark{width:78px;height:78px;border-radius:50%;background:#3d6f9a}
.brand-name{font-family:"Ubuntu",sans-serif;font-weight:700;font-size:50px;line-height:1;color:var(--white)}
.brand-sub{font-family:"Ubuntu",sans-serif;font-weight:700;font-size:8px;color:var(--white);margin-top:4px;letter-spacing:.2px}

.main-nav{left:361px;top:31px;height:74px;display:flex;align-items:center;font-size:11.5px;letter-spacing:.4px}
.main-nav a{padding:0 10px;border-left:1px solid var(--navy-line);line-height:28px}
.main-nav a.home{background:var(--light);color:var(--ink);width:85px;height:74px;line-height:74px;text-align:center;border:none;margin-right:12px}
.main-nav a.first{border-left:none}

.hero{left:64px;top:156px;width:783px;height:331px;background:var(--light)}
.hero-photo{left:0;top:0;width:486px;height:331px;background:linear-gradient(90deg,#c9cdd2 0%,#dfe3e7 35%,#d4e3ee 70%,#e2e6ea 100%)}
.hero-title{left:194px;top:72px;display:flex;align-items:center;gap:10px;color:var(--ink);font-family:"Ubuntu",sans-serif;font-weight:500;font-size:18px}
.hero-dot{width:36px;height:36px;border-radius:50%;background:#5b89b0}
.hero-copy{left:193px;top:124px;width:290px;color:var(--ink);font-size:13.5px;line-height:22px}
.hero-panel{left:486px;top:0;width:297px;height:281px;background:var(--orange)}
.hero-panel p{position:absolute;left:27px;top:38px;width:245px;font-size:13px;line-height:18.7px;text-align:justify;color:#fff8ea}
.btn-read{position:absolute;left:28px;top:177px;width:100px;height:38px;background:var(--light);color:var(--ink);font-size:13px;display:flex;align-items:center;justify-content:center}
.hero-controls{position:absolute;left:0;top:224px;width:297px;height:57px;border-top:2px solid var(--orange-dark);display:flex;align-items:center;padding-left:34px;font-family:"Ubuntu",sans-serif;font-weight:700;font-size:13px}
.hero-controls span{margin-right:21px}
.dots{display:flex;gap:9px;margin-left:10px}
.dots i{display:block;width:26px;height:26px;border-radius:50%;background:var(--light)}
.dots i.on{background:var(--navy-deep)}

.content{left:64px;top:488px;width:783px;height:520px;background:var(--navy-deep);border-left:1px solid var(--navy-line);border-right:1px solid var(--navy-line)}
.tabs{left:64px;top:488px;width:478px;height:60px;display:flex;border-bottom:1px solid var(--navy-line);font-size:11.5px;letter-spacing:.3px}
.tabs a{display:flex;align-items:center;justify-content:center;border-right:1px solid var(--navy-line)}
.tabs a.active{background:var(--white);color:var(--ink)}
.col-split{left:541px;top:488px;width:1px;height:520px;background:var(--navy-line)}
.welcome-photo{left:84px;top:566px;width:168px;height:188px;background:linear-gradient(160deg,#6d8fb4,#3a4b60 60%,#8a4a3c)}
.welcome-text{left:273px;top:570px;width:247px;font-size:11.5px;line-height:25px;text-align:justify}
.welcome-text b{font-size:13.5px;letter-spacing:.3px}
.row-split{left:64px;top:771px;width:478px;height:1px;background:var(--navy-line)}

.solutions{left:90px;top:792px}
.solutions h2{font-family:"Ubuntu",sans-serif;font-weight:400;font-size:23px}
.meta{font-size:8px;line-height:17px;margin-top:2px}
.sol-list{left:90px;top:868px;width:420px;display:grid;grid-template-columns:250px 1fr;row-gap:9px;font-size:11.5px}

.news-title{left:566px;top:503px;font-family:"Ubuntu",sans-serif;font-size:23px}
.news-item{left:567px;width:208px;font-size:11.5px;line-height:18px;text-align:justify}
.date{left:782px;width:46px;height:55px;background:var(--orange);color:var(--ink);text-align:center;font-family:"Ubuntu",sans-serif;line-height:1}
.date b{display:block;font-size:18px;margin-top:9px}
.date span{font-size:14px}
.more{left:571px;font-size:11.5px;display:flex;align-items:center;gap:6px}
.news-rule{left:562px;width:266px;height:1px;background:var(--navy-line)}

.skyline{left:0;top:948px;width:910px;height:62px;background:linear-gradient(180deg,rgba(228,228,228,0) 0%,rgba(228,228,228,.55) 55%,var(--light) 100%)}
.footer{left:0;top:1008px;width:910px;height:192px;background:var(--light)}
.label{left:109px;color:var(--ink);font-size:11.5px}
.field{left:164px;width:153px;height:24px;border:1px solid #cfcfcf;background:#e9e9e9;font-size:9px;color:var(--ink);padding:7px 9px}
.message{left:324px;top:1049px;width:153px;height:90px;border:1px solid #cfcfcf;background:#e9e9e9;font-size:9px;color:var(--ink);padding:6px 9px}
.submit{left:415px;top:1149px;width:62px;height:22px;background:var(--ink);color:var(--white);font-size:10px;display:flex;align-items:center;justify-content:center}
.foot-split{left:541px;top:1018px;width:1px;height:160px;background:#c6c6c6}
.foot-head{top:1044px;color:var(--ink);font-family:"Ubuntu",sans-serif;font-size:13.5px}
.foot-links{top:1074px;color:var(--ink);font-size:11.5px;line-height:24.5px}
.foot-links li{list-style:none;display:flex;align-items:center;gap:7px}
.copy{left:680px;top:1074px;color:var(--ink);font-size:10.5px;line-height:25px}
</style>
</head>
<body>
<div class="page">
  <div class="abs top-stripe"></div>
  <nav class="abs util-nav"><a href="#">SEARCH</a><span>|</span><a href="#">LOGIN OR REGISTER</a><span>|</span><a href="#">CONTACT US</a></nav>

  <div class="abs brand">
    <div class="brand-mark"></div>
    <div>
      <div class="brand-name">TKL</div>
      <div class="brand-sub">THE KINDLING LANTERN</div>
    </div>
  </div>

  <nav class="abs main-nav">
    <a class="home" href="#">HOME</a>
    <a class="first" href="#">OVERVIEW</a><a href="#">SERVICES</a><a href="#">SOLUTIONS</a><a href="#">SUPPORT</a><a href="#">PARTNERS</a>
  </nav>

  <section class="abs hero">
    <div class="abs hero-photo" role="img" aria-label="Boy looking up beside a teddy bear over a faint world map"></div>
    <div class="abs hero-title"><div class="hero-dot"></div>THE KINDLING LANTERN</div>
    <p class="abs hero-copy">Phasellus porta. Fusce suscipit varius mi. Lorem ipsum dolor sit amet, consec tetuer adipi scing elit.</p>
    <div class="abs hero-panel">
      <p>Phasellus porta. Fusce suscipit varius mi. Lorem ipsum dolor sit amet, consec tetuer adipi scing elit. Praesent vestibu lum molestie lacus. Aenean nonummy hendrerit mauris. Cum sociis na toque</p>
      <a class="btn-read" href="#">Read More</a>
      <div class="hero-controls"><span>PLAY</span><span>STOP</span>
        <div class="dots"><i class="on"></i><i></i><i></i><i></i></div>
      </div>
    </div>
  </section>

  <div class="abs content"></div>
  <nav class="abs tabs">
    <a class="active" href="#" style="width:93px">WELCOME</a>
    <a href="#" style="width:82px">HISTORY</a>
    <a href="#" style="width:95px">PARTNERS</a>
    <a href="#" style="width:121px">TESTIMONIALS</a>
    <a href="#" style="width:87px;border-right:none">SPECIALS</a>
  </nav>
  <div class="abs col-split"></div>

  <div class="abs welcome-photo" role="img" aria-label="Wexford Plaza towers covered in billboards"></div>
  <p class="abs welcome-text">Welcome to <b>THE KINDLING LANTERN</b> Lorem ipsum dolor sit amet, consec tetuer adipiscing elit. Praesent vestibulum molestie lacus. Aenean nonummy hendrerit mauris. Phasellus porta. Fusce suscipit varius mi. Cum sociis natoque penatibus et magnis dis parturient montes, mus.</p>
  <div class="abs row-split"></div>

  <div class="abs solutions">
    <h2>Solutions</h2>
    <div class="meta">Written by Administrator<br>Saturday, 07 July 2007 09:54</div>
  </div>
  <div class="abs sol-list">
    <span>→ Scientific and Risk Assessment</span><span>→ Change Management</span>
    <span>→ Information Technology</span><span>→ Strategic Communications</span>
    <span>→ Training and Education</span><span>→ Management Consulting</span>
  </div>

  <h2 class="abs news-title">News</h2>
  <p class="abs news-item" style="top:541px">02. 10. 2011 sit amet, consec teteur adipiscing elit. Praesent vestibu lum molestie lacus. Aenean nonum...</p>
  <div class="abs date" style="top:547px"><b>10</b><span>Feb</span></div>
  <a class="abs more" href="#" style="top:600px">» Read More</a>
  <div class="abs news-rule" style="top:626px"></div>

  <p class="abs news-item" style="top:651px">01. 28. 2011 dolor sit amet, consec teteur adipiscing elit. Praesent vestibu lum molestie lacus. Aenean non...</p>
  <div class="abs date" style="top:656px"><b>28</b><span>Jan</span></div>
  <a class="abs more" href="#" style="top:730px">» Read More</a>
  <div class="abs news-rule" style="top:770px"></div>

  <p class="abs news-item" style="top:801px">12. 17. 2010 dolor sit amet, consec teteur adipiscing elit. Praesent vestibu lum molestie lacus....</p>
  <div class="abs date" style="top:804px"><b>17</b><span>Dec</span></div>
  <a class="abs more" href="#" style="top:865px">» Read More</a>
  <div class="abs news-rule" style="top:901px"></div>
  <a class="abs more" href="#" style="left:562px;top:921px">See More News →</a>

  <div class="abs skyline" role="img" aria-label="Light city skyline silhouette"></div>

  <footer class="abs footer"></footer>
  <span class="abs label" style="top:1053px">Name:</span>
  <span class="abs label" style="top:1087px">Email:</span>
  <span class="abs label" style="top:1121px">Website:</span>
  <div class="abs field" style="top:1049px"></div>
  <div class="abs field" style="top:1082px"></div>
  <div class="abs field" style="top:1115px">http://</div>
  <div class="abs message">Enter your message here:</div>
  <a class="abs submit" href="#">SUBMIT</a>
  <div class="abs foot-split"></div>

  <h3 class="abs foot-head" style="left:575px;font-weight:400">CONNECT</h3>
  <ul class="abs foot-links" style="left:577px">
    <li>→ Chirpline</li><li>→ Friendsquare</li><li>→ Streamreel</li>
  </ul>
  <h3 class="abs foot-head" style="left:680px;font-weight:400">COPYRIGHT</h3>
  <div class="abs copy">The Kindling Lantern © 2011<br>Privacy Policy</div>
</div>
</body>
</html>
```